Asphalt Driveway Billboard Design

We need a billboard designed for an Asphalt & Concrete Company in Minnesota. We want to advertise Asphalt Driveways on this billboard! Logo is uploaded below. Our website is tamlin-paving.com for more information.

```html
<!DOCTYPE html>
<html lang="en">
<head>
<meta charset="utf-8">
<title>Tamlin Asphalt & Concrete Billboard</title>
<link href="https://fonts.googleapis.com/css2?family=Montserrat:wght@600;700;800&display=swap" rel="stylesheet">
<style>
  :root {
    --page-bg: #c6dcfb;
    --panel: #ffffff;
    --ink: #1d1d1f;
    --slate: #55585c;
    --brand-blue: #1467b3;
    --brand-blue-dark: #0c4f95;
    --arc-black: #151515;
    --arc-gray: #a9abae;
    --photo-sky: #c9d6e2;
    --photo-house: #8f9299;
    --photo-drive: #3c3f44;
  }
  * { margin: 0; padding: 0; box-sizing: border-box; }
  html, body { width: 1057px; height: 1200px; overflow: hidden; }
  body {
    background: var(--page-bg);
    font-family: "Montserrat", sans-serif;
    position: relative;
  }
  .billboard {
    position: absolute;
    left: 38px;
    top: 387px;
    width: 980px;
    height: 427px;
    overflow: hidden;
    box-shadow: 0 6px 14px rgba(0,0,0,0.25);
  }
  .house-photo {
    position: absolute;
    inset: 0;
    background: linear-gradient(180deg, var(--photo-sky) 0%, #b9c2cc 18%, var(--photo-house) 35%, #a2a5ab 60%, var(--photo-drive) 66%, #2f3236 100%);
  }
  .panel-shape { position: absolute; inset: 0; }
  .content {
    position: absolute;
    left: 590px;
    top: 0;
    width: 360px;
    height: 100%;
    text-align: center;
    color: var(--ink);
  }
  .brand { margin-top: 78px; display: flex; flex-direction: column; align-items: center; }
  .brand-name {
    font-weight: 800;
    font-size: 30px;
    letter-spacing: 1px;
    color: var(--ink);
    line-height: 1;
  }
  .brand-tag {
    font-weight: 700;
    font-size: 8px;
    letter-spacing: 1.5px;
    color: var(--ink);
    margin-top: 3px;
  }
  .headline {
    margin-top: 22px;
    font-weight: 800;
    font-size: 25px;
    line-height: 34px;
  }
  .headline .line-dark { color: var(--ink); display: block; }
  .headline .line-gray { color: var(--slate); display: block; }
  .tagline {
    margin: 9px auto 0;
    width: 334px;
    height: 26px;
    line-height: 26px;
    background: linear-gradient(90deg, var(--brand-blue-dark), var(--brand-blue));
    color: #fff;
    font-weight: 700;
    font-size: 11px;
    letter-spacing: 0.3px;
  }
  .services {
    display: flex;
    justify-content: center;
    margin-top: 14px;
  }
  .service {
    width: 112px;
    display: flex;
    flex-direction: column;
    align-items: center;
  }
  .service + .service { border-left: 1px solid #c9cbce; }
  .service-icon { width: 40px; height: 40px; }
  .service-label {
    margin-top: 8px;
    font-weight: 800;
    font-size: 12.5px;
    line-height: 18px;
    color: var(--brand-blue);
  }
  .contact {
    margin-top: 20px;
    display: flex;
    justify-content: center;
    align-items: center;
    gap: 8px;
    font-weight: 700;
    font-size: 16.5px;
    color: var(--ink);
  }
  .contact-item { display: flex; align-items: center; gap: 6px; }
  .contact-icon { width: 18px; height: 18px; }
  .divider { width: 2px; height: 20px; background: var(--ink); }
</style>
</head>
<body>
  <section class="billboard">
    <div class="house-photo" role="img" aria-label="Two-storey gray house with white garage doors and a freshly paved dark asphalt driveway"></div>

    <svg class="panel-shape" viewBox="0 0 980 427" aria-hidden="true">
      <path d="M466,427 Q470,40 702,0 L980,0 L980,427 Z" fill="var(--panel)"/>
      <path d="M472,430 Q476,42 708,-4" fill="none" stroke="var(--arc-black)" stroke-width="16"/>
      <path d="M503,430 Q508,70 770,-4" fill="none" stroke="var(--arc-gray)" stroke-width="16"/>
    </svg>

    <div class="content">
      <div class="brand">
        <span class="brand-name">TAMLIN</span>
        <span class="brand-tag">ASPHALT &amp; CONCRETE</span>
      </div>

      <h1 class="headline">
        <span class="line-dark">PREMIER ASPHALT &amp;</span>
        <span class="line-gray">CONCRETE CONTRACTOR</span>
      </h1>

      <p class="tagline">YOU DESERVE TO COME HOME TO QUALITY</p>

      <div class="services">
        <div class="service">
          <svg class="service-icon" viewBox="0 0 40 40" aria-hidden="true">
            <circle cx="20" cy="20" r="19" fill="var(--brand-blue)"/>
            <path d="M11,20 L20,12 L29,20 M14,18 V28 H26 V18" fill="none" stroke="#fff" stroke-width="2"/>
            <rect x="18" y="22" width="4" height="6" fill="#fff"/>
          </svg>
          <span class="service-label">ASPHALT<br>DRIVEWAYS</span>
        </div>
        <div class="service">
          <svg class="service-icon" viewBox="0 0 40 40" aria-hidden="true">
            <circle cx="20" cy="20" r="19" fill="var(--brand-blue)"/>
            <path d="M12,30 Q14,20 22,18 Q29,16 28,10" fill="none" stroke="#fff" stroke-width="6" stroke-linecap="round"/>
            <path d="M12,30 Q14,20 22,18 Q29,16 28,10" fill="none" stroke="var(--brand-blue)" stroke-width="1.4" stroke-dasharray="3 3"/>
          </svg>
          <span class="service-label">ASPHALT<br>ADDITIONS</span>
        </div>
        <div class="service">
          <svg class="service-icon" viewBox="0 0 40 40" aria-hidden="true">
            <circle cx="20" cy="20" r="19" fill="var(--brand-blue)"/>
            <path d="M17,13 H24 V17 H17 Z M19,17 V29 M15,29 H26" fill="none" stroke="#fff" stroke-width="2"/>
            <path d="M24,15 L29,12 M24,15 L29,15 M24,15 L29,18" stroke="#fff" stroke-width="1.4"/>
          </svg>
          <span class="service-label">ASPHALT<br>SEALCOATING</span>
        </div>
      </div>

      <div class="contact">
        <span class="contact-item">
          <svg class="contact-icon" viewBox="0 0 18 18" aria-hidden="true">
            <circle cx="9" cy="9" r="9" fill="var(--ink)"/>
            <path d="M6,4.5 L7.6,4.5 L8.3,7 L7.2,7.9 Q8.3,10.2 10.1,10.8 L11,9.7 L13.5,10.4 L13.5,12 Q12.5,13.5 10.5,13 Q5.5,11.5 4.8,6.5 Q4.8,5 6,4.5 Z" fill="#fff"/>
          </svg>
          763-555-0148
        </span>
        <span class="divider"></span>
        <span class="contact-item">
          <svg class="contact-icon" viewBox="0 0 18 18" aria-hidden="true">
            <circle cx="9" cy="9" r="9" fill="var(--ink)"/>
            <circle cx="9" cy="9" r="5" fill="none" stroke="#fff" stroke-width="1.2"/>
            <path d="M4,9 H14 M9,4 Q6,9 9,14 M9,4 Q12,9 9,14" fill="none" stroke="#fff" stroke-width="1"/>
          </svg>
          tamlin-paving.com
        </span>
      </div>
    </div>
  </section>
</body>
</html>
```